Brookvale Homes Flyer

Quarter-page leave-behind flyer for a commercial cleaning company (print)

ABOUT US
Quillon Commercial Cleaning is a Texas-owned commercial cleaning company serving Austin for over 20 years. We were recently named to Brookvale Homes's Capital Partner Roster Circle, a preferred vendor program covering apartment communities across the Austin metro. Our sales team will hand this flyer to apartment community managers during property visits.

THE JOB THIS FLYER MUST DO
A busy property manager should scan it in five seconds, understand what we do, trust us and keep the card on their desk. The call to action is booking a free walkthrough of their community. Do not include any pricing.

SPECS
Size: 4.25 x 5.5 inches (quarter of a letter page), single sided, portrait. Print ready with 0.125 inch bleed, CMYK, 300 dpi minimum. Vector preferred.

REQUIRED CONTENT
Headline: The clean your residents notice.
Badge or tagline: Brookvale Homes's Approved Austin Cleaning Company.
Supporting line: Preferred Vendor Partner in BVH's Capital Partner Roster Circle. Texas-owned, serving Austin for 20+ years.
Services (icons welcome): recurring janitorial, floor strip wax and buff, carpet extraction, windows and glass, upholstery care, pressure washing, move-in and move-out cleans, damage restoration.
Trust points: licensed and insured, background-checked crews, TrudeLink compliant, invoicing through Supplier Nook and Halvex Systems.

Social proof line: Already trusted by BVH communities. Ask your peers at The Wendlow and The Fennick on Garrow.

Call to action: Book a free walkthrough of your community. Call or email 512-555-0147 or support@quillonclean-example.com

STYLE DIRECTION
Clean, crisp and premium. Whiteness and shine should feel like part of the message. We like a deep green and teal palette with one warm accent, but strong alternative directions are welcome. Custom icons over clip art.
AVOID
Stock photos of cleaners with buckets, cartoon mascots, sparkle overload, cluttered layouts, any prices or dollar amounts.
DELIVERABLES
Print-ready PDF with bleed and crop marks, plus editable source files (AI, PSD or Figma). A version with our logo placement marked, since we will supply the logo file to the winner.

```html
<!DOCTYPE html>
<html lang="en">
<head>
<meta charset="utf-8">
<title>Quillon Commercial Cleaning – Brookvale Homes Flyer</title>
<link href="https://fonts.googleapis.com/css2?family=Poppins:wght@400;500;600;700;800&family=Roboto:wght@400;500&display=swap" rel="stylesheet">
<style>
  :root {
    --teal: #05504f;
    --teal-deep: #04413f;
    --green: #3cb54a;
    --ink: #1d1d1d;
    --text: #2b2b2b;
    --rule: #d9dcdc;
    --paper: #ffffff;
    --mist: #f3f4f4;
  }
  * { margin: 0; padding: 0; box-sizing: border-box; }
  html, body { width: 927px; height: 1200px; overflow: hidden; background: var(--paper); }
  .flyer {
    position: relative; width: 927px; height: 1200px; overflow: hidden;
    font-family: 'Roboto', sans-serif; color: var(--text); background: var(--paper);
  }

  /* Hero */
  .hero-photo {
    position: absolute; left: 0; top: 0; width: 927px; height: 472px;
    background: linear-gradient(100deg, #eceeee 0%, #f7f7f7 45%, #e9e6e3 75%, #d9d4cf 100%);
  }
  .hero-corner { position: absolute; right: 0; top: 0; z-index: 2; }
  .headline {
    position: absolute; left: 88px; top: 54px; z-index: 2;
    font-family: 'Poppins', sans-serif; font-weight: 800;
    font-size: 52px; line-height: 58px; letter-spacing: -1.5px; color: var(--ink);
  }
  .headline .accent { color: var(--green); }
  .headline-rule { position: absolute; left: 88px; top: 241px; width: 82px; height: 4px; background: var(--green); border-radius: 2px; z-index: 2; }
  .approval {
    position: absolute; left: 88px; top: 260px; width: 420px; z-index: 2;
    font-family: 'Poppins', sans-serif; font-weight: 700; font-size: 21px; line-height: 29px; color: var(--ink);
  }
  .supporting {
    position: absolute; left: 88px; top: 331px; width: 350px; z-index: 2;
    font-family: 'Poppins', sans-serif; font-size: 14px; line-height: 22px; color: var(--text);
  }
  .brand-name {
    position: absolute; left: 574px; top: 150px; z-index: 2;
    font-family: 'Poppins', sans-serif; font-weight: 700; font-size: 56px; color: var(--green); letter-spacing: -1px;
  }

  .service-banner {
    position: absolute; left: 172px; top: 439px; width: 584px; height: 64px; z-index: 5;
    background: var(--paper); border-radius: 32px;
  }
  .service-banner span {
    position: absolute; left: 6px; top: 6px; right: 6px; bottom: 6px;
    background: var(--teal); border-radius: 26px;
    display: flex; align-items: center; justify-content: center;
    font-family: 'Poppins', sans-serif; font-weight: 700; font-size: 18px; color: #fff;
  }

  /* Services */
  .services { position: absolute; left: 0; top: 472px; width: 927px; height: 402px; z-index: 1;
    background: linear-gradient(180deg, #ffffff 0%, #ffffff 70%, #f2f4f4 100%); }
  .service { position: absolute; width: 180px; text-align: center; }
  .service .icon {
    width: 84px; height: 84px; margin: 0 auto; border: 1.6px solid var(--green); border-radius: 50%;
    display: flex; align-items: center; justify-content: center; background: #fff;
  }
  .service .icon svg { width: 44px; height: 44px; fill: none; stroke: var(--green); stroke-width: 1.6; stroke-linecap: round; stroke-linejoin: round; }
  .service .label { margin-top: 9px; font-size: 17.5px; line-height: 22px; color: var(--text); }
  .divider-v { position: absolute; width: 1px; height: 116px; background: var(--rule); }
  .divider-h { position: absolute; left: 89px; top: 207px; width: 749px; height: 1px; background: var(--rule); }

  /* Trust band */
  .trust { position: absolute; left: 0; top: 874px; width: 927px; height: 82px; display: flex; }
  .trust-item { flex: 1; display: flex; align-items: center; gap: 12px; padding-left: 17px; color: #fff;
    font-size: 16px; line-height: 22px; font-weight: 500; background: var(--teal); }
  .trust-item:nth-child(even) { background: var(--teal-deep); }
  .trust-item svg { width: 28px; height: 28px; flex: none; fill: none; stroke: #fff; stroke-width: 1.8; stroke-linecap: round; stroke-linejoin: round; }

  /* Proof */
  .proof { position: absolute; left: 0; top: 956px; width: 927px; height: 116px; background: var(--mist); }
  .proof-icon { position: absolute; left: 42px; top: 21px; width: 61px; height: 61px; border: 1.6px solid var(--green); border-radius: 50%;
    display: flex; align-items: center; justify-content: center; }
  .proof-icon svg { width: 30px; height: 30px; fill: none; stroke: var(--green); stroke-width: 1.8; }
  .proof-lead { position: absolute; left: 116px; top: 19px; font-size: 15.5px; color: var(--ink); }
  .proof-ask { position: absolute; left: 116px; top: 42px; font-family: 'Roboto', sans-serif; font-weight: 500;
    font-size: 21.5px; line-height: 29px; color: var(--green); }
  .partner-name { position: absolute; left: 575px; top: 26px; width: 92px; text-align: center;
    font-family: 'Poppins', sans-serif; font-weight: 700; font-size: 30px; line-height: 56px; color: var(--green); }
  .partner-rule { position: absolute; left: 684px; top: 30px; width: 1px; height: 52px; background: #c9cccc; }
  .partner-program { position: absolute; left: 702px; top: 28px; font-size: 21px; line-height: 30px; color: var(--ink); }

  /* CTA */
  .cta { position: absolute; left: 0; top: 1072px; width: 927px; height: 128px; background: var(--teal); }
  .cta-shape { position: absolute; left: 0; top: 0; }
  .cta-title { position: absolute; left: 51px; top: 28px; font-family: 'Poppins', sans-serif; color: #fff;
    font-size: 29px; line-height: 38px; letter-spacing: -0.2px; }
  .cta-title strong { font-weight: 700; display: block; }
  .cta-title span { font-weight: 500; display: block; }
  .cta-contact { position: absolute; left: 611px; top: 20px; color: #fff; }
  .cta-contact .kicker { font-size: 17px; letter-spacing: 0.5px; font-weight: 500; }
  .cta-contact .phone { font-family: 'Poppins', sans-serif; font-weight: 800; font-size: 29px; line-height: 40px; margin-top: 2px; }
  .cta-contact .email { font-size: 17.5px; margin-top: -1px; }
</style>
</head>
<body>
<main class="flyer">

  <section class="hero">
    <div class="hero-photo" role="img" aria-label="Bright white apartment lounge with two modern armchairs and a small round side table"></div>
    <svg class="hero-corner" width="150" height="184" viewBox="0 0 150 184" aria-hidden="true">
      <path d="M0 0 H150 V182 C138 90 90 18 0 0 Z" fill="var(--teal)"/>
    </svg>

    <h1 class="headline">THE CLEAN<br>YOUR RESIDENTS<br><span class="accent">NOTICE</span></h1>
    <div class="headline-rule"></div>
    <p class="approval">Brookvale Homes's Approved Austin Cleaning Company</p>
    <p class="supporting">Preferred Vendor Partner in BVH's Capital Partner Roster Circle. Texas-owned, serving Austin for 20+ years.</p>

    <div class="brand-name">Quillon</div>
  </section>

  <section class="services">
    <div class="service" style="left:92px; top:56px;">
      <div class="icon"><svg viewBox="0 0 44 44"><path d="M6 38h32M9 38V16h9v22M18 38V9h10v29M28 38V20h7v18"/><path d="M12 20h3M12 25h3M12 30h3M21 13h4M21 18h4M21 23h4M21 28h4M31 24h1M31 29h1"/></svg></div>
      <div class="label">Recurring<br>Janitorial</div>
    </div>
    <div class="service" style="left:280px; top:56px;">
      <div class="icon"><svg viewBox="0 0 44 44"><path d="M26 6l-6 20"/><path d="M14 26h12l4 10H10z"/><path d="M14 36l1-5M19 36v-5M24 36l-1-5"/><circle cx="33" cy="20" r="2"/><circle cx="36" cy="30" r="1.5"/><path d="M9 14v4M7 16h4"/></svg></div>
      <div class="label">Floor Strip<br>Wax and Buff</div>
    </div>
    <div class="service" style="left:467px; top:56px;">
      <div class="icon"><svg viewBox="0 0 44 44"><rect x="8" y="10" width="28" height="14" rx="2"/><path d="M18 24v4h8v-4M22 28v10"/><path d="M12 14v6M16 14v6M28 14v6M32 14v6"/><path d="M22 4v3M20.5 5.5h3"/></svg></div>
      <div class="label">Carpet<br>Extraction</div>
    </div>
    <div class="service" style="left:654px; top:56px;">
      <div class="icon"><svg viewBox="0 0 44 44"><rect x="10" y="6" width="24" height="30"/><path d="M22 6v30M10 21h24M7 36h30"/><path d="M15 12l4-4M26 16l5-5"/></svg></div>
      <div class="label">Windows<br>and Glass</div>
    </div>

    <div class="divider-v" style="left:281px; top:66px;"></div>
    <div class="divider-v" style="left:463px; top:66px;"></div>
    <div class="divider-v" style="left:652px; top:66px;"></div>
    <div class="divider-h"></div>

    <div class="service" style="left:92px; top:231px;">
      <div class="icon"><svg viewBox="0 0 44 44"><path d="M15 22V12a3 3 0 0 1 3-3h8a3 3 0 0 1 3 3v10"/><path d="M11 22h22v8H11z"/><path d="M13 30v5M31 30v5"/><path d="M36 10v4M34 12h4M8 16v3"/></svg></div>
      <div class="label">Upholstery<br>Care</div>
    </div>
    <div class="service" style="left:280px; top:231px;">
      <div class="icon"><svg viewBox="0 0 44 44"><rect x="8" y="18" width="16" height="16" rx="2"/><path d="M12 18v-5h8v5"/><circle cx="12" cy="36" r="2"/><circle cx="22" cy="36" r="2"/><path d="M24 24c6 0 8-4 8-10l4-4"/><path d="M37 14l3 2M38 9h3"/></svg></div>
      <div class="label">Pressure<br>Washing</div>
    </div>
    <div class="service" style="left:467px; top:231px;">
      <div class="icon"><svg viewBox="0 0 44 44"><path d="M12 30l12-18 10 8-10 16z"/><path d="M16 24l4 3M19 20l4 3M22 16l4 3"/><path d="M8 12v4M6 14h4M36 30v4M34 32h4"/></svg></div>
      <div class="label">Move-in And<br>Move-out Cleans</div>
    </div>
    <div class="service" style="left:654px; top:231px;">
      <div class="icon"><svg viewBox="0 0 44 44"><circle cx="16" cy="16" r="5"/><path d="M16 7v3M16 22v3M7 16h3M22 16h3M10 10l2 2M20 20l2 2M10 22l2-2M20 12l2-2"/><circle cx="29" cy="29" r="4"/><path d="M29 21v3M29 34v3M21 29h3M34 29h3"/></svg></div>
      <div class="label">Damage<br>Restoration</div>
    </div>

    <div class="divider-v" style="left:281px; top:248px;"></div>
    <div class="divider-v" style="left:463px; top:248px;"></div>
    <div class="divider-v" style="left:652px; top:248px;"></div>
  </section>

  <div class="service-banner"><span>Full-Service Cleaning For Apartment Communities</span></div>

  <section class="trust">
    <div class="trust-item"><svg viewBox="0 0 28 28"><circle cx="13" cy="15" r="11"/><path d="M8 15l4 4 12-14"/></svg><span>Licensed And<br>Insured</span></div>
    <div class="trust-item"><svg viewBox="0 0 28 28"><circle cx="13" cy="15" r="11"/><path d="M8 15l4 4 12-14"/></svg><span>Background<br>Checked Crews</span></div>
    <div class="trust-item"><svg viewBox="0 0 28 28"><circle cx="13" cy="15" r="11"/><path d="M8 15l4 4 12-14"/></svg><span>TrudeLink<br>Compliant</span></div>
    <div class="trust-item" style="flex:1.1"><svg viewBox="0 0 28 28"><circle cx="13" cy="15" r="11"/><path d="M8 15l4 4 12-14"/></svg><span>Invoicing Through<br>Supplier Nook</span></div>
    <div class="trust-item" style="flex:1.2"><svg viewBox="0 0 28 28"><circle cx="13" cy="15" r="11"/><path d="M8 15l4 4 12-14"/></svg><span>Halvex<br>Systems</span></div>
  </section>

  <section class="proof">
    <div class="proof-icon"><svg viewBox="0 0 30 30"><path d="M5 27h20M8 27V10h8v17M16 27V5h7v22M11 14h2M11 19h2M19 10h1M19 15h1M19 20h1"/></svg></div>
    <p class="proof-lead">Already trusted by BVH communities.</p>
    <p class="proof-ask">Ask your peers at The Wendlow<br>and The Fennick on Garrow.</p>
    <div class="partner-name">BVH</div>
    <div class="partner-rule"></div>
    <p class="partner-program">Capital Partner<br>Roster Circle</p>
  </section>

  <section class="cta">
    <svg class="cta-shape" width="927" height="128" viewBox="0 0 927 128" aria-hidden="true">
      <path d="M0 0 H580 L532 128 H40 C20 128 0 110 0 90 Z" fill="#064a49"/>
      <path d="M578 0 L531 128" stroke="#fff" stroke-width="9"/>
      <circle cx="553" cy="66" r="40" fill="#fff"/>
      <circle cx="553" cy="66" r="32" fill="var(--green)"/>
      <path d="M542 52c-3 2-4 6-1 11 3 6 8 11 13 13 5 2 8 1 10-2l-5-5-4 2c-3-1-6-4-8-8l2-4z" fill="#fff"/>
      <path d="M556 52a9 9 0 0 1 8 8M556 46a15 15 0 0 1 14 14" fill="none" stroke="#fff" stroke-width="2" stroke-linecap="round"/>
    </svg>
    <h2 class="cta-title"><strong>BOOK A FREE WALKTHROUGH</strong><span>OF YOUR COMMUNITY</span></h2>
    <div class="cta-contact">
      <div class="kicker">CALL OR EMAIL</div>
      <div class="phone">512-555-0147</div>
      <div class="email">support@quillonclean-example.com</div>
    </div>
  </section>

</main>
</body>
</html>
```